Verdal Group Business Card Design

The CEO is looking for a new trendy look for his business card.
You can stay with current branding or come up with something new/creative. It can be 3D, including Medical Office buildings. You can use our logo in a variety of colors. Please include name, title, company name, company website, email address, cell number

Target Market(s)

Real Estate Development and Construction

Industry/Entity Type

Health care real estate

Contact Information for Business Card

Rohesh Kamble, CEO M-702.418.6293 E-roheshkamble@verdal.example Address:4100 Lanyard St, Tampa, FL 33611 www.verdal.example

Other font styles liked:
• Be creative

Requirements
Must have
• Creative, trendy look
Nice to have
• Please go to our website to get a feel- www. verdal.example
Should not have
• small fonts

```html
<!DOCTYPE html>
<html lang="en">
<head>
<meta charset="utf-8">
<title>Verdal Group Business Card</title>
<link href="https://fonts.googleapis.com/css2?family=Montserrat:wght@400;700;800&display=swap" rel="stylesheet">
<style>
  :root {
    --stage: #1d1d1f;
    --paper: #ffffff;
    --brand-red: #c0303f;
    --brand-navy: #2b3a5c;
    --text-grey: #6f6f73;
    --card-black: #1a1a1b;
  }
  html, body {
    margin: 0;
    padding: 0;
    width: 1200px;
    height: 780px;
    overflow: hidden;
    background: var(--stage);
    font-family: "Montserrat", sans-serif;
  }
  .stage {
    position: relative;
    width: 1200px;
    height: 780px;
    display: flex;
    justify-content: center;
    align-items: center;
    gap: 90px;
  }
  .card {
    position: relative;
    width: 360px;
    height: 630px;
    box-sizing: border-box;
    overflow: hidden;
  }
  .card-front {
    background: var(--paper);
  }
  .edge-band {
    position: absolute;
    left: 0;
    top: 0;
    bottom: 0;
    width: 18px;
    background: var(--brand-red);
  }
  .edge-line {
    position: absolute;
    left: 24px;
    top: 0;
    bottom: 0;
    width: 4px;
    background: var(--brand-navy);
  }
  .wordmark {
    position: absolute;
    right: 34px;
    top: 70px;
    margin: 0;
    font-weight: 800;
    font-size: 40px;
    line-height: 1;
    color: var(--brand-red);
    letter-spacing: -0.5px;
    text-align: right;
  }
  .contact-block {
    position: absolute;
    left: 62px;
    right: 24px;
    bottom: 56px;
  }
  .person-name {
    margin: 0;
    font-weight: 800;
    font-size: 25px;
    color: var(--brand-red);
    letter-spacing: 0.5px;
    text-transform: uppercase;
  }
  .person-title {
    margin: 2px 0 22px;
    font-weight: 700;
    font-size: 19px;
    color: var(--brand-navy);
  }
  .address {
    margin: 0 0 14px;
    font-style: normal;
    font-size: 16px;
    line-height: 1.3;
    color: var(--text-grey);
  }
  .contact-list {
    list-style: none;
    margin: 0;
    padding: 0;
    font-size: 15px;
    color: var(--text-grey);
  }
  .contact-list li {
    display: flex;
    align-items: center;
    gap: 9px;
    line-height: 1.55;
  }
  .contact-icon {
    width: 14px;
    height: 14px;
    flex: none;
  }
  .card-back {
    background: var(--card-black);
  }
  .pattern-fill {
    position: absolute;
    inset: 0;
    background: linear-gradient(200deg, #9a9a9c 0%, #5a5a5c 30%, #2c2c2e 60%, #141415 100%);
  }
</style>
</head>
<body>
<main class="stage">
  <section class="card card-front" aria-label="Business card front">
    <div class="edge-band"></div>
    <div class="edge-line"></div>
    <h1 class="wordmark">Verdal Group</h1>
    <div class="contact-block">
      <h2 class="person-name">Rohesh Kamble</h2>
      <p class="person-title">CEO</p>
      <address class="address">4100 Lanyard St,<br>Tampa, FL 33611</address>
      <ul class="contact-list">
        <li>
          <svg class="contact-icon" viewBox="0 0 14 14" aria-hidden="true">
            <rect x="3" y="0.8" width="8" height="12.4" rx="1.5" fill="none" stroke="var(--brand-red)" stroke-width="1.6"/>
            <circle cx="7" cy="10.6" r="0.9" fill="var(--brand-red)"/>
          </svg>
          702.418.6293
        </li>
        <li>
          <svg class="contact-icon" viewBox="0 0 14 14" aria-hidden="true">
            <rect x="0.5" y="2.5" width="13" height="9" fill="var(--brand-red)"/>
            <polyline points="0.5,2.5 7,8 13.5,2.5" fill="none" stroke="#fff" stroke-width="1.2"/>
          </svg>
          roheshkamble@verdal.example
        </li>
        <li>
          <svg class="contact-icon" viewBox="0 0 14 14" aria-hidden="true">
            <circle cx="7" cy="7" r="6.5" fill="var(--brand-red)"/>
            <ellipse cx="7" cy="7" rx="2.6" ry="6.5" fill="none" stroke="#fff" stroke-width="0.9"/>
            <line x1="0.5" y1="7" x2="13.5" y2="7" stroke="#fff" stroke-width="0.9"/>
          </svg>
          www.verdal.example
        </li>
      </ul>
    </div>
  </section>

  <section class="card card-back" aria-label="Business card back">
    <div class="pattern-fill" role="img" aria-label="Repeating brand mark pattern in glossy spot varnish on black, with one red mark near the lower centre"></div>
  </section>
</main>
</body>
</html>
```